Help us share the power of history

We need 5 flyers (they can be similar in design, just small content changes in the front) and 1 large poster.

Paper Lantern? is a movement that aims to change the history market so that everyone gets what they need to be a changemaker of society. We've been selected as one of the most promising startups in Massachusetts and we will have a booth at Brightforge's Pitch Day.

We are trying to attract the attention of people walking buy to invest in our kickstarter campaign.

Target Market(s)

500-1,000 social entrepreneurs who are going to be walking around a large convention hall - so everything in terms of colors and design needs to be attractive

Industry/Entity Type

Non Profit

Font styles to use
Other font styles liked:
• Phoenix American

Colors

Designer to choose colors to be used in the design.

Requirements
Must have
• Font type: Phoenix American
• Modern
• Easy to read
• Eye-catching
• Please see attached document for more information.

```html
<!DOCTYPE html>
<html lang="en">
<head>
<meta charset="utf-8">
<title>Paper Lantern? — Vitamin Flyers</title>
<link rel="stylesheet" href="https://fonts.googleapis.com/css2?family=Big+Shoulders+Display:wght@300;400&family=Jost:wght@400;600&display=swap">
<style>
  :root {
    --backdrop: #707070;
    --ink: #ffffff;
    --ink-shadow: rgba(40, 20, 0, 0.55);
    --card-shadow: rgba(0, 0, 0, 0.45);

    --orange-edge: #ff7700;
    --orange-glow: #ffa04a;
    --green-edge: #04a61c;
    --green-glow: #00e324;
    --red-edge: #bd160e;
    --red-glow: #ff1c12;
    --yellow-edge: #d2ab13;
    --yellow-glow: #f2c81c;
    --purple-edge: #8f10c2;
    --purple-glow: #c63ff2;

    --display: "Big Shoulders Display", "Arial Narrow", sans-serif;
    --body: "Jost", "Century Gothic", sans-serif;
  }

  * { box-sizing: border-box; margin: 0; padding: 0; }

  html, body {
    width: 1200px;
    height: 2635px;
    overflow: hidden;
    background: var(--backdrop);
  }

  .flyer-sheet {
    position: relative;
    width: 1200px;
    height: 2635px;
  }

  .card {
    position: absolute;
    width: 453px;
    height: 453px;
    border-radius: 72px;
    box-shadow: 0 8px 14px var(--card-shadow), 0 2px 4px rgba(0,0,0,0.3);
    color: var(--ink);
    overflow: hidden;
  }

  .card--front { left: 109px; }
  .card--back  { left: 634px; }

  .row-1 { top: 77px; }
  .row-2 { top: 585px; }
  .row-3 { top: 1084px; }
  .row-4 { top: 1599px; }
  .row-5 { top: 2122px; }

  .theme-community { --edge: var(--orange-edge); --glow: var(--orange-glow); }
  .theme-agency    { --edge: var(--green-edge);  --glow: var(--green-glow); }
  .theme-empathy   { --edge: var(--red-edge);    --glow: var(--red-glow); }
  .theme-imagination { --edge: var(--yellow-edge); --glow: var(--yellow-glow); }
  .theme-context   { --edge: var(--purple-edge); --glow: var(--purple-glow); }

  .card {
    background: linear-gradient(180deg, var(--edge) 0%, var(--edge) 18%, var(--glow) 45%, var(--edge) 78%, var(--edge) 100%);
  }

  .card-art {
    position: absolute;
    inset: 0;
    width: 453px;
    height: 453px;
  }

  .title-text {
    font-family: var(--display);
    font-weight: 400;
    fill: var(--ink);
    stroke: rgba(60, 30, 0, 0.35);
    stroke-width: 1.2;
    paint-order: stroke;
  }

  .url-text {
    font-family: var(--display);
    font-weight: 400;
    fill: var(--ink);
    stroke: rgba(60, 30, 0, 0.3);
    stroke-width: 1;
    paint-order: stroke;
  }

  .tagline {
    position: absolute;
    left: 0;
    right: 0;
    top: 345px;
    text-align: center;
    font-family: var(--body);
    font-weight: 600;
    font-size: 29px;
    line-height: 1;
    text-shadow: 0 1px 2px var(--ink-shadow);
  }

  .appeal {
    position: absolute;
    left: 0;
    right: 0;
    top: 145px;
    text-align: center;
    font-family: var(--body);
    font-weight: 400;
    font-size: 27px;
    line-height: 33px;
    text-shadow: 0 1px 2px var(--ink-shadow);
  }
</style>
</head>
<body>
<main class="flyer-sheet">

  <svg width="0" height="0" style="position:absolute" aria-hidden="true">
    <defs>
      <filter id="lift" x="-10%" y="-10%" width="120%" height="130%">
        <feDropShadow dx="0" dy="2" stdDeviation="2" flood-color="#2a1400" flood-opacity="0.5"/>
      </filter>
    </defs>
  </svg>

  <!-- Community -->
  <section class="card card--front theme-community row-1">
    <svg class="card-art" viewBox="0 0 453 453">
      <g filter="url(#lift)">
        <text class="title-text" x="226.5" y="204" text-anchor="middle" font-size="138" textLength="257" lengthAdjust="spacingAndGlyphs">VITAMIN</text>
        <text class="title-text" x="226.5" y="323" text-anchor="middle" font-size="144" textLength="381" lengthAdjust="spacingAndGlyphs">COMMUNITY</text>
      </g>
    </svg>
    <p class="tagline">You belong here.</p>
  </section>
  <section class="card card--back theme-community row-1">
    <p class="appeal">Support our movement<br>and help us build Boston’s<br>first AR map</p>
    <svg class="card-art" viewBox="0 0 453 453">
      <text class="url-text" x="226.5" y="312" text-anchor="middle" font-size="54" textLength="360" lengthAdjust="spacingAndGlyphs" filter="url(#lift)">WWW.PAPER-LANTERN.ORG</text>
    </svg>
  </section>

  <!-- Agency -->
  <section class="card card--front theme-agency row-2">
    <svg class="card-art" viewBox="0 0 453 453">
      <g filter="url(#lift)">
        <text class="title-text" x="226.5" y="204" text-anchor="middle" font-size="138" textLength="257" lengthAdjust="spacingAndGlyphs">VITAMIN</text>
        <text class="title-text" x="226.5" y="323" text-anchor="middle" font-size="144" textLength="241" lengthAdjust="spacingAndGlyphs">AGENCY</text>
      </g>
    </svg>
    <p class="tagline">You have power.</p>
  </section>
  <section class="card card--back theme-agency row-2">
    <p class="appeal">Support our movement<br>and help us build Boston’s<br>first AR map</p>
    <svg class="card-art" viewBox="0 0 453 453">
      <text class="url-text" x="226.5" y="312" text-anchor="middle" font-size="54" textLength="360" lengthAdjust="spacingAndGlyphs" filter="url(#lift)">WWW.PAPER-LANTERN.ORG</text>
    </svg>
  </section>

  <!-- Empathy -->
  <section class="card card--front theme-empathy row-3">
    <svg class="card-art" viewBox="0 0 453 453">
      <g filter="url(#lift)">
        <text class="title-text" x="226.5" y="204" text-anchor="middle" font-size="138" textLength="257" lengthAdjust="spacingAndGlyphs">VITAMIN</text>
        <text class="title-text" x="226.5" y="323" text-anchor="middle" font-size="144" textLength="290" lengthAdjust="spacingAndGlyphs">EMPATHY</text>
      </g>
    </svg>
    <p class="tagline">We all matter.</p>
  </section>
  <section class="card card--back theme-empathy row-3">
    <p class="appeal">Support our movement<br>and help us build Boston’s<br>first AR map</p>
    <svg class="card-art" viewBox="0 0 453 453">
      <text class="url-text" x="226.5" y="312" text-anchor="middle" font-size="54" textLength="360" lengthAdjust="spacingAndGlyphs" filter="url(#lift)">WWW.PAPER-LANTERN.ORG</text>
    </svg>
  </section>

  <!-- Imagination -->
  <section class="card card--front theme-imagination row-4">
    <svg class="card-art" viewBox="0 0 453 453">
      <g filter="url(#lift)">
        <text class="title-text" x="226.5" y="204" text-anchor="middle" font-size="138" textLength="257" lengthAdjust="spacingAndGlyphs">VITAMIN</text>
        <text class="title-text" x="226.5" y="323" text-anchor="middle" font-size="144" textLength="404" lengthAdjust="spacingAndGlyphs">IMAGINATION</text>
      </g>
    </svg>
    <p class="tagline">Dare to dream.</p>
  </section>
  <section class="card card--back theme-imagination row-4">
    <p class="appeal">Support our movement<br>and help us build Boston’s<br>first AR map</p>
    <svg class="card-art" viewBox="0 0 453 453">
      <text class="url-text" x="226.5" y="312" text-anchor="middle" font-size="54" textLength="360" lengthAdjust="spacingAndGlyphs" filter="url(#lift)">WWW.PAPER-LANTERN.ORG</text>
    </svg>
  </section>

  <!-- Context -->
  <section class="card card--front theme-context row-5">
    <svg class="card-art" viewBox="0 0 453 453">
      <g filter="url(#lift)">
        <text class="title-text" x="226.5" y="204" text-anchor="middle" font-size="138" textLength="257" lengthAdjust="spacingAndGlyphs">VITAMIN</text>
        <text class="title-text" x="226.5" y="323" text-anchor="middle" font-size="144" textLength="260" lengthAdjust="spacingAndGlyphs">CONTEXT</text>
      </g>
    </svg>
    <p class="tagline" style="font-size:25px">You understand the full picture.</p>
  </section>
  <section class="card card--back theme-context row-5">
    <p class="appeal">Support our movement<br>and help us build Boston’s<br>first AR map</p>
    <svg class="card-art" viewBox="0 0 453 453">
      <text class="url-text" x="226.5" y="312" text-anchor="middle" font-size="54" textLength="360" lengthAdjust="spacingAndGlyphs" filter="url(#lift)">WWW.PAPER-LANTERN.ORG</text>
    </svg>
  </section>

</main>
</body>
</html>
```